Building company business card

Design and print business cards for BRENTHOLM PTY LTD.
A residantial homes building company.
Mark Lantern already designed the company Logo.

```html
<!DOCTYPE html>
<html lang="en">
<head>
<meta charset="utf-8">
<title>BRENTHOLM PTY LTD — Business Card</title>
<link href="https://fonts.googleapis.com/css2?family=Carlito:wght@400;700&display=swap" rel="stylesheet">
<style>
  :root {
    --backdrop: #adadad;
    --card-white: #ffffff;
    --navy: #172566;
    --gold: #b98a2e;
    --gold-light: #d9aa4f;
    --grey-text: #7a7a7a;
    --rule: #a5a5a5;
  }
  * { margin: 0; padding: 0; box-sizing: border-box; }
  html, body {
    width: 1200px; height: 1000px; overflow: hidden;
    background: var(--backdrop);
    font-family: "Carlito", "Calibri", sans-serif;
  }
  .card {
    position: absolute; left: 294px; width: 613px; height: 352px;
    border-radius: 24px;
  }
  .card--front { top: 118px; background: var(--card-white); }
  .card--back { top: 530px; background: var(--navy); }

  .brand {
    position: absolute; display: flex; align-items: center; gap: 14px;
  }
  .card--front .brand { left: 0; right: 0; top: 54px; justify-content: center; }
  .brand__mark { width: 34px; height: 34px; border-radius: 50%; background: linear-gradient(135deg, var(--gold-light), var(--gold)); }
  .brand__name { font-weight: 700; font-size: 46px; line-height: 1; letter-spacing: 1px; color: var(--navy); }

  .identity {
    position: absolute; right: 321px; top: 180px; text-align: right;
  }
  .identity__name { font-weight: 700; font-size: 19px; color: var(--navy); letter-spacing: 0.3px; }
  .identity__role { font-weight: 700; font-size: 16px; color: var(--gold); margin-top: 1px; }

  .divider-v {
    position: absolute; left: 306px; top: 163px; width: 2px; height: 75px; background: #b5b5b5;
  }
  .contacts { position: absolute; left: 320px; top: 167px; list-style: none; }
  .contacts li { display: flex; align-items: center; gap: 7px; height: 22px; font-size: 17px; color: var(--navy); }
  .contacts svg { width: 13px; height: 13px; fill: var(--gold); flex: none; }

  .divider-h { position: absolute; left: 84px; right: 83px; top: 293px; height: 2px; background: var(--rule); }
  .address { position: absolute; left: 0; right: 0; top: 309px; text-align: center; font-size: 16px; color: var(--grey-text); }

  .card--back .brand { left: 0; right: 0; top: 84px; flex-direction: column; gap: 28px; }
  .card--back .brand__mark { width: 110px; height: 110px; }
  .card--back .brand__name { font-size: 50px; color: #ffffff; }
</style>
</head>
<body>
  <section class="card card--front">
    <div class="brand">
      <span class="brand__mark"></span>
      <span class="brand__name">BRENTHOLM</span>
    </div>

    <div class="identity">
      <p class="identity__name">DORIAN (Dory) KESTEL</p>
      <p class="identity__role">Director</p>
    </div>
    <div class="divider-v"></div>
    <ul class="contacts">
      <li><svg viewBox="0 0 12 14"><path d="M3 0h6a1.5 1.5 0 0 1 1.5 1.5v11A1.5 1.5 0 0 1 9 14H3a1.5 1.5 0 0 1-1.5-1.5v-11A1.5 1.5 0 0 1 3 0zm0 1.5v9h6v-9zm3 10a.8.8 0 1 0 0 1.6.8.8 0 0 0 0-1.6z"/></svg>0431 582 907</li>
      <li><svg viewBox="0 0 14 14"><path d="M3 0l2.5 3.2-1.3 1.6a8 8 0 0 0 5 5l1.6-1.3L14 11l-1.6 2.4C7 14 0 7 .6 1.6z"/></svg>0462 318 540</li>
      <li><svg viewBox="0 0 14 10"><path d="M0 0h14v10H0zm1.3 1.2L7 5.6l5.7-4.4z"/></svg>dk@brentholm-pl.com</li>
    </ul>

    <div class="divider-h"></div>
    <p class="address">CDB-U 48215, PO Box 264, Harlow Heights, Vic 3209</p>
  </section>

  <section class="card card--back">
    <div class="brand">
      <span class="brand__mark"></span>
      <span class="brand__name">BRENTHOLM</span>
    </div>
  </section>
</body>
</html>
```